Business Card Design for Mabel's Pantry

We make food for dogs.
Business Card Design (using the logo designed by you). Our Brand color is a bright canary yellow. For example our signage is predominantly yellow, with the logo in black. I'd like the card also to use that imagery.
Feel free to use the two sides creatively.
Vertical Design is also great.

Industry/Entity Type

Pet food

Contact Information for Business Card

Name, email, website, phone no

Font styles to use
Sans Serif

Colors
59FF00
82FF00
B8FF75
E3FFCB
F4FFEA
FFF300
FFF600
FEFA6F
FFFEC7
FFFEE8

Requirements
Nice to have
• A graphic in the same brush stroke style of the logo shoeing a doggy bowl of food

```html
<!DOCTYPE html>
<html lang="en">
<head>
<meta charset="utf-8">
<title>Mabel's Pantry – Business Card</title>
<link rel="stylesheet" href="https://fonts.googleapis.com/css2?family=Oswald:wght@400&family=Montserrat:wght@700&family=Raleway:wght@400&display=swap">
<style>
  :root {
    --backdrop: #dcdcdc;
    --canary-top: #ffe83a;
    --canary-bottom: #fcc91c;
    --ink: #111111;
    --ink-soft: #2a2a2a;
    --graphic-fade: rgba(60, 45, 5, 0.55);
  }
  * { margin: 0; padding: 0; box-sizing: border-box; }
  html, body {
    width: 1200px; height: 800px; overflow: hidden;
    background: var(--backdrop);
  }
  .canvas { position: relative; width: 1200px; height: 800px; }

  .card {
    position: absolute;
    width: 282px; height: 493px;
    border-radius: 32px;
    background: linear-gradient(180deg, var(--canary-top) 0%, var(--canary-bottom) 100%);
    color: var(--ink);
    text-align: center;
    overflow: hidden;
  }
  .card--front { left: 291px; top: 228px; }
  .card--back  { left: 628px; top: 79px; }

  .brand-dot {
    position: absolute; left: 50%;
    width: 26px; height: 26px; margin-left: -13px;
    border-radius: 50%; background: var(--ink);
  }
  .brand-name {
    position: absolute; left: 0; right: 0;
    font-family: "Oswald", sans-serif; font-weight: 400;
    font-size: 34px; line-height: 1; letter-spacing: 0.5px;
    text-transform: uppercase; white-space: nowrap;
  }
  .card--front .brand-dot { top: 138px; }
  .card--front .brand-name { top: 186px; }
  .card--back .brand-dot { top: 98px; }
  .card--back .brand-name { top: 146px; }

  .front-graphic {
    position: absolute; left: 15px; right: 0; top: 297px; bottom: 0;
    border-top-left-radius: 40px;
    background: linear-gradient(180deg, rgba(60, 45, 5, 0) 0%, var(--graphic-fade) 100%);
  }

  .holder-name {
    position: absolute; left: 0; right: 0; top: 258px;
    font-family: "Montserrat", sans-serif; font-weight: 700;
    font-size: 21px; letter-spacing: -0.3px; color: var(--ink-soft);
    text-transform: uppercase;
  }
  .holder-title {
    position: absolute; left: 0; right: 0; top: 284px;
    font-family: "Raleway", sans-serif; font-size: 14px; color: var(--ink-soft);
    letter-spacing: 0.3px;
  }

  .contact-divider {
    position: absolute; left: 39px; top: 311px;
    width: 204px; height: 18px;
  }
  .contact-list, .address {
    position: absolute; left: 0; right: 0;
    font-family: "Raleway", sans-serif; font-size: 13.5px; font-style: normal;
    line-height: 19.5px; color: var(--ink-soft); list-style: none;
  }
  .contact-list { top: 341px; }
  .rule {
    position: absolute; left: 50px; width: 182px; top: 405px;
    height: 1px; background: var(--ink-soft);
  }
  .address { top: 412px; font-size: 14px; }
</style>
</head>
<body>
<main class="canvas">

  <section class="card card--front" aria-label="Card front">
    <span class="brand-dot" aria-hidden="true"></span>
    <p class="brand-name">Mabel's Pantry</p>
    <div class="front-graphic" role="img" aria-label="Large black brush-stroke brand graphic, cropped at the bottom of the card"></div>
  </section>

  <section class="card card--back" aria-label="Card back">
    <span class="brand-dot" aria-hidden="true"></span>
    <p class="brand-name">Mabel's Pantry</p>

    <h1 class="holder-name">Daniel Harper</h1>
    <p class="holder-title">Managing Director</p>

    <svg class="contact-divider" viewBox="0 0 204 18" aria-hidden="true">
      <line x1="0" y1="9" x2="60" y2="9" stroke="#2a2a2a" stroke-width="1"/>
      <line x1="144" y1="9" x2="204" y2="9" stroke="#2a2a2a" stroke-width="1"/>
      <rect x="63" y="0" width="17" height="18" rx="3" fill="#2a2a2a"/>
      <path d="M67 4.5c1-.8 2-.6 2.4.3l.7 1.6c.2.6 0 1-.5 1.4l-.6.5c.6 1.4 1.6 2.5 3 3.2l.5-.6c.4-.5.9-.6 1.4-.4l1.6.8c.8.4 1 1.4.2 2.3-1 1-2.5 1.1-4 .3-2.6-1.4-4.5-3.6-5.300-6.3-.4-1.3-.2-2.4.6-3.1z" fill="#fcd62a"/>
      <rect x="84" y="0" width="17" height="18" rx="3" fill="#2a2a2a"/>
      <rect x="86.5" y="5" width="12" height="8.5" fill="none" stroke="#fcd62a" stroke-width="1.1"/>
      <polyline points="86.5,5 92.5,10 98.5,5" fill="none" stroke="#fcd62a" stroke-width="1.1"/>
      <rect x="105" y="0" width="17" height="18" rx="3" fill="#2a2a2a"/>
      <circle cx="113.5" cy="9" r="5.5" fill="none" stroke="#fcd62a" stroke-width="1.1"/>
      <ellipse cx="113.5" cy="9" rx="2.3" ry="5.5" fill="none" stroke="#fcd62a" stroke-width="0.9"/>
      <line x1="108" y1="9" x2="119" y2="9" stroke="#fcd62a" stroke-width="0.9"/>
    </svg>

    <ul class="contact-list">
      <li>044-555 201 348</li>
      <li>hello@mabelspantry.com</li>
      <li>www.mabelspantry.com</li>
    </ul>

    <span class="rule" aria-hidden="true"></span>

    <address class="address">
      18 Willow Lane, Suite 4<br>
      Brookfield, 45210
    </address>
  </section>

</main>
</body>
</html>
```